Business Card Design Project

Business and Appointment Card for Medical Practice. On back of card we would like to have: blank line for patient name, Mon-Fri each with a check box next to the day, blank line for appointment date, blank line for appointment time, with option to circle am or pm.

Target Market(s)

Professional Business Associates, as well as function as patient appointment cards (on back side of card)

Industry/Entity Type

Business

Colors

```html
<!DOCTYPE html>
<html lang="en">
<head>
<meta charset="utf-8">
<title>Rowan Hill Medical Associates – Business &amp; Appointment Card</title>
<link rel="stylesheet" href="https://fonts.googleapis.com/css2?family=Crimson+Text:wght@400;600&display=swap">
<style>
  :root {
    --cherry: #a3161f;
    --leaf: #1f7a3a;
    --paper: #ffffff;
    --ground: #e9ece9;
    --rule-soft: #9bb5a2;
    --shadow: rgba(20, 40, 25, 0.18);
  }
  * { box-sizing: border-box; margin: 0; padding: 0; }
  html, body {
    width: 1200px; height: 767px; overflow: hidden;
    background: var(--ground);
    font-family: "Crimson Text", Georgia, serif;
  }
  .sheet { position: relative; width: 1200px; height: 767px; }

  .card {
    position: absolute; top: 229px;
    width: 540px; height: 309px;
    background: var(--paper);
    box-shadow: 0 10px 28px var(--shadow);
  }
  .card--front { left: 40px; }
  .card--back  { left: 620px; }

  /* brand block */
  .brand { position: absolute; display: flex; align-items: center; gap: 12px; }
  .brand__dot { width: 40px; height: 40px; border-radius: 50%; background: var(--cherry); flex: none; }
  .brand__name {
    color: var(--cherry); font-weight: 600; line-height: 1.05;
    font-size: 26px; letter-spacing: 0.5px;
  }
  .brand__name span { display: block; font-size: 17px; letter-spacing: 2px; }
  .card--front .brand { left: 26px; top: 178px; }
  .card--back  .brand { left: 30px; top: 212px; }

  /* front: contacts */
  .contacts { position: absolute; right: 22px; top: 22px; list-style: none; }
  .contacts li {
    display: flex; justify-content: flex-end; align-items: center; gap: 10px;
    color: var(--leaf); font-size: 14px; height: 24px;
  }
  .contacts svg { width: 18px; height: 18px; }

  .front-rule { position: absolute; left: 238px; right: 0; top: 170px; border-top: 1.5px solid var(--leaf); }
  .person { position: absolute; left: 300px; top: 138px; color: var(--cherry); font-size: 19px; }
  .role { position: absolute; left: 300px; top: 178px; color: var(--leaf); font-size: 19px; }
  .address { position: absolute; color: var(--cherry); font-size: 12px; }
  .card--front .address { left: 26px; bottom: 16px; }

  /* back: appointment form */
  .field { position: absolute; left: 30px; display: flex; align-items: flex-end; gap: 8px; color: var(--leaf); font-size: 14px; }
  .field__line { border-bottom: 1px dotted var(--rule-soft); height: 14px; }
  .field--patient { top: 24px; }
  .field--patient .field__line { width: 370px; }
  .field--date { top: 66px; }
  .field--date .field__line { width: 130px; }
  .field--time { top: 140px; }
  .field--time .field__line { width: 130px; }

  .days { position: absolute; left: 290px; top: 62px; display: grid; grid-template-columns: repeat(4, 56px); row-gap: 12px; }
  .choice { display: flex; align-items: center; gap: 5px; color: var(--leaf); font-size: 11px; letter-spacing: 0.5px; }
  .box { width: 12px; height: 12px; border: 1.3px solid var(--cherry); border-radius: 2px; }
  .meridiem { position: absolute; left: 290px; top: 140px; display: flex; gap: 18px; }

  .back-rule { position: absolute; left: 250px; right: 30px; top: 178px; border-top: 1.5px solid var(--leaf); }
  .card--back .address { right: 30px; top: 196px; text-align: right; line-height: 1.35; }
</style>
</head>
<body>
<main class="sheet">

  <section class="card card--front" aria-label="Business card front">
    <ul class="contacts">
      <li>+1 555-210-4870
        <svg viewBox="0 0 20 20" aria-hidden="true"><circle cx="10" cy="10" r="10" fill="#a3161f"/><path d="M6.5 5.5c1 0 1.4 1.8 1 2.3l-.6.6c.5 1.3 1.4 2.2 2.7 2.7l.6-.6c.5-.4 2.3 0 2.3 1 0 1-.8 2-2 2-3.5 0-6-2.6-6-6 0-1.2 1-2 2-2z" fill="#fff"/></svg></li>
      <li>info@rowanhillmedical.com
        <svg viewBox="0 0 20 20" aria-hidden="true"><circle cx="10" cy="10" r="10" fill="#a3161f"/><rect x="5" y="6.5" width="10" height="7" fill="none" stroke="#fff" stroke-width="1.2"/><path d="M5 6.5l5 4 5-4" fill="none" stroke="#fff" stroke-width="1.2"/></svg></li>
      <li>www.rowanhillmedical.com
        <svg viewBox="0 0 20 20" aria-hidden="true"><circle cx="10" cy="10" r="10" fill="#a3161f"/><circle cx="10" cy="10" r="5" fill="none" stroke="#fff" stroke-width="1.2"/><path d="M5 10h10M10 5c-2.5 3-2.5 7 0 10M10 5c2.5 3 2.5 7 0 10" fill="none" stroke="#fff" stroke-width="1"/></svg></li>
    </ul>

    <div class="front-rule"></div>
    <p class="person">Daniel Reyes M.D (Dental)</p>
    <p class="role">Dental Surgeon</p>

    <div class="brand">
      <span class="brand__dot" aria-hidden="true"></span>
      <p class="brand__name">Rowan Hill<span>Medical Associates</span></p>
    </div>
    <p class="address">48 Orchard Lane, Springdale, PA 15000</p>
  </section>

  <section class="card card--back" aria-label="Appointment card back">
    <div class="field field--patient">Patient Name <span class="field__line"></span></div>
    <div class="field field--date">Appointment Date <span class="field__line"></span></div>

    <div class="days">
      <span class="choice"><span class="box"></span>MON</span>
      <span class="choice"><span class="box"></span>TUE</span>
      <span class="choice"><span class="box"></span>WED</span>
      <span class="choice"><span class="box"></span>THU</span>
      <span class="choice"><span class="box"></span>FRI</span>
      <span class="choice"><span class="box"></span>SAT</span>
      <span class="choice"><span class="box"></span>SUN</span>
    </div>

    <div class="field field--time">Appointment Time <span class="field__line"></span></div>
    <div class="meridiem">
      <span class="choice"><span class="box"></span>AM</span>
      <span class="choice"><span class="box"></span>PM</span>
    </div>

    <div class="back-rule"></div>
    <div class="brand">
      <span class="brand__dot" aria-hidden="true"></span>
      <p class="brand__name">Rowan Hill<span>Medical Associates</span></p>
    </div>
    <p class="address">48 Orchard Lane<br>Springdale<br>PA 15000</p>
  </section>

</main>
</body>
</html>
```